HomeBridle business card and stationary design

We are looking for a simple yet elegant design for our mortgage company business card and stationary.

The card should include:
Name (Derek Walsh)
Title (CEO)
Phone Number (614-208-3917)
Address (48 Birchfield Court, Suite 314, Marlow, OH 43952)
Email (email@homebridle-example.com)
"NMLS" i.e. (NMLS 61947)
"Company NMLS" (Company NMLS 472815)

See above

```html
<!DOCTYPE html>
<html lang="en">
<head>
<meta charset="utf-8">
<title>HomeBridle Business Card</title>
<link href="https://fonts.googleapis.com/css2?family=Montserrat:wght@500;700&family=Roboto:wght@400&display=swap" rel="stylesheet">
<style>
  :root {
    --page-bg: #c9c9c9;
    --card-white: #ffffff;
    --navy: #1a2633;
    --sky: #00aeef;
    --ink: #1c2530;
    --grey-text: #4a4f55;
    --rule: #2a2f35;
  }
  html, body {
    margin: 0;
    padding: 0;
    width: 1200px;
    height: 1200px;
    overflow: hidden;
    background: var(--page-bg);
  }
  .canvas {
    position: relative;
    width: 1200px;
    height: 1200px;
  }
  .card {
    position: absolute;
    left: 262px;
    width: 686px;
    height: 392px;
    overflow: hidden;
  }
  .card-front { top: 165px; background: var(--card-white); }
  .card-back { top: 653px; background: var(--navy); }

  .edge-band {
    position: absolute;
    left: 0; top: 0;
    width: 14px; height: 392px;
  }

  .brand-name {
    position: absolute;
    left: 48px;
    top: 70px;
    margin: 0;
    font-family: "Montserrat", sans-serif;
    font-weight: 500;
    font-size: 46px;
    line-height: 1;
    color: var(--ink);
    letter-spacing: 0.2px;
  }

  .person {
    position: absolute;
    right: 42px;
    top: 212px;
    text-align: right;
  }
  .person-name {
    margin: 0;
    font-family: "Montserrat", sans-serif;
    font-weight: 700;
    font-size: 22px;
    line-height: 1.1;
    color: var(--ink);
  }
  .person-title {
    margin: 3px 0 0;
    font-family: "Roboto", sans-serif;
    font-size: 15px;
    color: var(--sky);
  }

  .divider {
    position: absolute;
    left: 48px;
    right: 42px;
    top: 267px;
    height: 0;
    border-top: 1px solid var(--rule);
  }

  .contact-list, .address {
    position: absolute;
    top: 277px;
    margin: 0;
    padding: 0;
    list-style: none;
    font-family: "Roboto", sans-serif;
    font-size: 15.5px;
    line-height: 19.5px;
    color: var(--grey-text);
  }
  .contact-list { left: 48px; }
  .contact-list li { display: flex; align-items: center; gap: 6px; }
  .contact-list .icon { width: 13px; height: 13px; flex: none; }
  .contact-list .company-nmls { margin-top: 2px; }

  .address {
    right: 42px;
    top: 273px;
    text-align: right;
    font-style: normal;
  }
  .address .nmls { display: block; margin-top: 6px; }

  .back-brand {
    position: absolute;
    right: 77px;
    top: 273px;
    text-align: right;
  }
  .back-name {
    margin: 0;
    font-family: "Montserrat", sans-serif;
    font-weight: 500;
    font-size: 50px;
    line-height: 1;
    color: #ffffff;
  }
  .back-url {
    margin: 8px 0 0;
    font-family: "Montserrat", sans-serif;
    font-weight: 500;
    font-size: 12px;
    letter-spacing: 5px;
    margin-right: -5px;
    color: #ffffff;
  }
</style>
</head>
<body>
<div class="canvas">

  <section class="card card-front">
    <svg class="edge-band" viewBox="0 0 14 392" aria-hidden="true">
      <polygon points="0,0 14,0 14,162 0,168" fill="var(--sky)"/>
      <polygon points="0,172 14,166 14,392 0,392" fill="var(--navy)"/>
    </svg>

    <h1 class="brand-name">HomeBridle</h1>

    <div class="person">
      <p class="person-name">Derek Walsh</p>
      <p class="person-title">CEO</p>
    </div>

    <div class="divider"></div>

    <ul class="contact-list">
      <li>
        <svg class="icon" viewBox="0 0 16 16" aria-hidden="true"><path fill="var(--sky)" d="M3.6 1.2l2.3 2.5-1.2 1.8c.9 2 2.6 3.8 4.7 4.8l1.8-1.2 2.6 2.3-1.3 2.4C7.2 13.5 2.5 8.8 1.2 3z"/></svg>
        <span>614-208-3917</span>
      </li>
      <li>
        <svg class="icon" viewBox="0 0 16 16" aria-hidden="true"><rect x="1" y="3.5" width="14" height="9" fill="var(--sky)"/><path d="M1.5 4l6.5 5 6.5-5" fill="none" stroke="#fff" stroke-width="1.2"/></svg>
        <span>info@homebridle-example.com</span>
      </li>
      <li>
        <svg class="icon" viewBox="0 0 16 16" aria-hidden="true"><circle cx="8" cy="8" r="7" fill="var(--sky)"/><path d="M5 4c1 1 2 1 2 3s-2 1-2 3M10 3c-1 2 1 3 3 3M9 14c0-2 1-3 3-3" fill="none" stroke="#fff" stroke-width="1.2"/></svg>
        <span>homebridle-example.com</span>
      </li>
      <li class="company-nmls">Company NMLS 472815</li>
    </ul>

    <address class="address">
      48 Birchfield Court<br>
      Suite 314<br>
      Marlow, OH 43952
      <span class="nmls">NMLS I.E. 61947</span>
    </address>
  </section>

  <section class="card card-back">
    <div class="back-brand">
      <p class="back-name">HomeBridle</p>
      <p class="back-url">www.homebridle-example.com</p>
    </div>
  </section>

</div>
</body>
</html>
```